"Copper Kettle" Moonshine 6-Pack Shipper Design

We're looking for a 6-pack shipper design for our moonshine brand - "Copper Kettle". We're looking for a classic look printed with black ink on regular uncoated cardboard.

Attached are a couple examples, the die line that the file will need to be designed within, and our brand label artwork to be used.

Thank you!

```html
<!DOCTYPE html>
<html lang="en">
<head>
<meta charset="utf-8">
<title>Copper Kettle Moonshine – 6-Pack Shipper Dieline</title>
<link href="https://fonts.googleapis.com/css2?family=Arvo:wght@400;700&family=Ultra&display=swap" rel="stylesheet">
<style>
  :root{
    --page:#e9e9e9;
    --board:#e4e4e4;
    --ink:#111111;
    --paper:#eeeeee;
    --cut:#3a3a3a;
    --fold:#d23a3a;
    --art:#8a8a8a;
  }
  *{box-sizing:border-box;margin:0;padding:0}
  html,body{width:1200px;height:1200px;overflow:hidden;background:var(--page)}
  .dieline{position:relative;width:1200px;height:1200px}
  .flap,.panel,.glue-tab{position:absolute}
  .flap{background:var(--board);border:1px solid var(--cut)}
  .panel{border-top:1px dashed var(--fold);border-bottom:1px dashed var(--fold);display:flex}
  .panel--front{background:var(--board)}
  .panel--label{background:var(--ink);color:var(--paper)}
  .glue-tab{left:1143px;top:463px;width:36px;height:275px}

  .brand{font-family:"Ultra",serif;font-weight:400;line-height:.95;letter-spacing:.5px}
  .slab{font-family:"Arvo",serif}

  /* label panel */
  .label{margin:14px 12px;flex:1;border:1px solid var(--paper);border-radius:8px;display:flex;flex-direction:column;align-items:center;padding:10px 8px;text-align:center}
  .label__crafted{font:700 7px "Arvo",serif;letter-spacing:1px}
  .label__town{font:400 10px "Arvo",serif;border:1px solid var(--paper);border-radius:10px;padding:1px 10px;margin-top:2px;letter-spacing:1px}
  .label__name{font-size:36px;margin:16px 0 8px}
  .label__stars{font-size:9px;letter-spacing:9px;margin-bottom:8px}
  .label__type{font:700 13px "Arvo",serif;letter-spacing:1px;border-top:1px solid var(--paper);border-bottom:1px solid var(--paper);padding:2px 10px}
  .label__spirits{font:400 6.5px "Arvo",serif;letter-spacing:.5px;margin-top:4px}
  .stats{display:flex;gap:8px;align-items:center;border:1px solid currentColor;border-radius:12px;padding:2px 12px;margin-top:8px;font:700 8px "Arvo",serif}
  .stats small{display:block;font-size:5px;font-weight:400;text-align:center}

  /* front panel */
  .bottle-art{margin:22px 0 0 14px;width:98px;height:234px;border-radius:40px 40px 18px 18px;background:linear-gradient(180deg,#9a9a9a,#6e6e6e)}
  .front__copy{flex:1;display:flex;flex-direction:column;align-items:center;padding:18px 10px 0 12px;color:var(--ink);text-align:center}
  .front__count{font:700 16px "Arvo",serif;letter-spacing:1px;align-self:flex-end;margin-right:30px}
  .front__name{font-size:42px;margin-top:10px}
  .front__stars{font-size:10px;letter-spacing:10px;margin-top:8px}
  .front__type{font:700 13px "Arvo",serif;letter-spacing:2px;margin-top:6px}
  .badge{background:var(--ink);color:var(--paper);border-radius:6px;padding:5px 14px 4px;text-align:center}
  .badge__name{font-size:17px;letter-spacing:.5px}
  .badge__sub{font:700 8px "Arvo",serif;letter-spacing:1.5px;margin-top:2px}
  .front__copy .badge{margin-top:8px;width:186px}

  .flap--badge{display:flex;justify-content:center;align-items:flex-start;padding-top:30px}
  .flap--badge .badge{width:268px;padding:8px 14px 6px}
  .flap--badge .badge__name{font-size:23px}
  .flap--badge .badge__sub{font-size:10px}

  .flap--spec{display:flex;flex-direction:column;align-items:center;padding-top:28px;transform:rotate(180deg);transform-origin:center}
  .flap--spec .spec{font:700 10px "Arvo",serif;letter-spacing:1px;color:var(--ink);margin-top:12px}
  .flap--spec .stats{color:var(--ink);margin-top:0;font-size:9px}
</style>
</head>
<body>
<main class="dieline">

  <!-- top flaps -->
  <div class="flap" style="left:20px;top:349px;width:217px;height:114px"></div>
  <div class="flap flap--badge" style="left:248px;top:349px;width:327px;height:114px">
    <div class="badge"><div class="badge__name brand">COPPERKETTLE</div><div class="badge__sub">TENNESSEE MOONSHINE</div></div>
  </div>
  <div class="flap" style="left:585px;top:349px;width:216px;height:114px"></div>
  <div class="flap" style="left:810px;top:349px;width:327px;height:114px">
    <div class="flap--spec" style="position:absolute;inset:0;padding-top:0;justify-content:flex-end;padding-bottom:0">
      <div class="spec" style="margin-bottom:24px">SPIRITS DISTILLED FROM GRAIN &amp; CANE</div>
      <div class="stats" style="order:2;margin-bottom:4px">
        <span>40%<small>ABV</small></span>•<span>80<small>PROOF</small></span>•<span>750<small>ML</small></span>
      </div>
    </div>
  </div>

  <!-- main panels -->
  <section class="panel panel--label" style="left:20px;top:463px;width:223px;height:275px">
    <div class="label">
      <div class="label__crafted">CRAFTED IN</div>
      <div class="label__town">★ MILLBROOK TN ★</div>
      <div class="label__name brand">Copper<br>Kettle</div>
      <div class="label__stars">★★★★★★★</div>
      <div class="label__type">TN MOONSHINE</div>
      <div class="label__spirits">SPIRITS DISTILLED FROM GRAIN &amp; CANE</div>
      <div class="stats"><span>40%<small>ABV</small></span>•<span>80<small>PROOF</small></span>•<span>750<small>ML</small></span></div>
    </div>
  </section>

  <section class="panel panel--front" style="left:243px;top:463px;width:337px;height:275px">
    <div class="bottle-art" role="img" aria-label="Illustration of a moonshine jug with handle wearing the brand label"></div>
    <div class="front__copy">
      <div class="front__count">6 x 750 ml</div>
      <div class="front__name brand">Copper<br>Kettle</div>
      <div class="front__stars">★★★★★★★★</div>
      <div class="front__type">TN MOONSHINE</div>
      <div class="badge"><div class="badge__name brand">COPPERKETTLE</div><div class="badge__sub">TENNESSEE MOONSHINE</div></div>
    </div>
  </section>

  <section class="panel panel--label" style="left:580px;top:463px;width:225px;height:275px">
    <div class="label">
      <div class="label__crafted">CRAFTED IN</div>
      <div class="label__town">★ MILLBROOK TN ★</div>
      <div class="label__name brand">Copper<br>Kettle</div>
      <div class="label__stars">★★★★★★★</div>
      <div class="label__type">TN MOONSHINE</div>
      <div class="label__spirits">SPIRITS DISTILLED FROM GRAIN &amp; CANE</div>
      <div class="stats"><span>40%<small>ABV</small></span>•<span>80<small>PROOF</small></span>•<span>750<small>ML</small></span></div>
    </div>
  </section>

  <section class="panel panel--front" style="left:805px;top:463px;width:338px;height:275px;border-right:1px dashed var(--fold)">
    <div class="bottle-art" role="img" aria-label="Illustration of a moonshine jug with handle wearing the brand label"></div>
    <div class="front__copy">
      <div class="front__count">6 x 750 ml</div>
      <div class="front__name brand">Copper<br>Kettle</div>
      <div class="front__stars">★★★★★★★★</div>
      <div class="front__type">TN MOONSHINE</div>
      <div class="badge"><div class="badge__name brand">COPPERKETTLE</div><div class="badge__sub">TENNESSEE MOONSHINE</div></div>
    </div>
  </section>

  <svg class="glue-tab" viewBox="0 0 36 275" aria-hidden="true">
    <polygon points="0,1 34,8 34,262 0,274" fill="var(--board)" stroke="var(--cut)" stroke-width="1"/>
  </svg>

  <!-- bottom flaps -->
  <div class="flap" style="left:20px;top:738px;width:217px;height:114px"></div>
  <div class="flap" style="left:248px;top:738px;width:327px;height:114px"></div>
  <div class="flap" style="left:585px;top:738px;width:216px;height:114px"></div>
  <div class="flap" style="left:810px;top:738px;width:327px;height:114px"></div>

</main>
</body>
</html>
```